Coffee roasting needs homepage with web shop

small roasting (no cafe!) needs a simple website with a web shop. We sell coffee to dealers and end customers. The shop should be for end consumers as well as for B2B customers. A login should be available. The design should be modern and at the same time classic with subtle (dark) colors. We need the tabs "Coffee, Shop, Contact, Coffee, Coffee, Login, About Us, Imprint, Privacy" Logo nr 1 should be used from attached file

Target Market(s)

B2B

Number of Pages Required

5+ page

Font styles to use
Sans Serif

Colors

Designer to choose only greyscale colors for use in the design.

Requirements
Must have
• Webshop

```html
<!DOCTYPE html>
<html lang="en">
<head>
<meta charset="utf-8">
<title>Brennwerk Coffee Roasters</title>
<link rel="stylesheet" href="https://fonts.googleapis.com/css2?family=Oswald:wght@400;500;600&family=Open+Sans:wght@400;600;700&family=Playfair+Display:ital@1&display=swap">
<style>
:root{
  --sidebar:#ffffff;
  --ink:#1a1a1a;
  --page:#161616;
  --panel:#1d1d1d;
  --footer:#202020;
  --text:#d8d8d8;
  --muted:#9a9a9a;
  --accent:#b27a4b;
  --accent-dark:#8a5a33;
  --white:#ffffff;
}
*{box-sizing:border-box;margin:0;padding:0}
html,body{width:1200px;height:2756px;overflow:hidden}
body{position:relative;background:var(--page);font-family:"Open Sans",Arial,sans-serif;color:var(--text)}
.abs{position:absolute}

/* Sidebar */
.sidebar{left:0;top:0;width:232px;height:2756px;background:var(--sidebar)}
.side-block{position:absolute;left:0;width:232px}
.brand{position:absolute;left:22px;top:34px;width:150px;height:150px;border:3px solid var(--ink);border-radius:50%;display:flex;align-items:center;justify-content:center;font-family:"Oswald",sans-serif;font-weight:500;font-size:27px;color:var(--ink)}
.side-nav{position:absolute;left:88px;top:266px;list-style:none}
.side-nav li{font-family:"Oswald",sans-serif;font-weight:500;font-size:17px;letter-spacing:1px;color:var(--ink);height:42px}
.side-nav li.current{color:var(--accent)}
.side-nav li.gap{margin-top:26px}
.side-social{position:absolute;left:72px;top:616px;display:flex;gap:10px}
.side-social span{width:22px;height:22px;border:2px solid var(--accent);border-radius:50%}

/* Hero */
.hero{left:232px;top:0;width:968px;height:560px;background:linear-gradient(160deg,#d9d2c8 0%,#a88f74 35%,#5a3f2a 65%,#2d1e14 100%)}
.hero-title{right:40px;top:372px;text-align:right;font-family:"Oswald",sans-serif;font-weight:600;font-size:68px;line-height:74px;color:var(--white);letter-spacing:1px}

/* Section heads */
.kicker{font-family:"Playfair Display",serif;font-style:italic;font-size:22px;color:var(--accent)}
.heading{font-family:"Oswald",sans-serif;font-weight:500;font-size:44px;color:var(--white);letter-spacing:1px}
.rule{height:3px;width:64px;background:var(--accent)}

/* Products */
.product-img{top:812px;width:280px;height:208px}
.product{top:1058px;width:280px}
.product h3{font-family:"Oswald",sans-serif;font-weight:500;font-size:19px;color:var(--white);letter-spacing:.5px}
.product h3 .price{margin-left:16px;font-weight:400}
.product p{margin-top:8px;font-size:12px;line-height:19px;color:var(--muted)}
.product .more{margin-top:20px;font-family:"Oswald",sans-serif;font-size:13px;letter-spacing:1px;color:var(--text)}
.arrows{display:flex;gap:28px}
.arrows svg{width:34px;height:20px}

/* About */
.about{left:232px;top:1352px;width:968px;height:508px;background:linear-gradient(90deg,#2b2b2b 0%,#3a3a3a 45%,#1c1c1c 100%)}
.about-img{left:328px;top:1420px;width:264px;height:340px;background:linear-gradient(180deg,#3c3028 0%,#e4ddd4 60%,#8b7a6a 100%)}
.about-text{left:648px;top:1625px;width:420px;font-size:13px;line-height:21px;color:var(--text)}
.btn{display:inline-block;background:var(--accent);color:var(--white);font-family:"Oswald",sans-serif;font-size:15px;letter-spacing:1.5px;text-align:center}

/* Roasted */
.roast-img{top:2112px;height:200px}
.roast-label{left:592px;top:2190px;width:248px;text-align:center;font-family:"Oswald",sans-serif;font-weight:500;font-size:20px;color:var(--white)}
.roast-label small{display:block;font-family:"Open Sans",sans-serif;font-weight:400;font-size:11px;color:var(--text)}

/* Footer */
.footer{left:232px;top:2500px;width:968px;height:256px;background:var(--footer)}
.foot-head{font-family:"Oswald",sans-serif;font-weight:500;font-size:17px;color:var(--white);letter-spacing:1px}
.foot-list{list-style:none;font-size:13px;line-height:24px;color:var(--muted)}
.foot-social{display:flex;gap:10px}
.foot-social span{width:26px;height:26px;border:2px solid var(--muted);border-radius:50%}
.foot-brand{left:1048px;top:2530px;width:112px;height:112px;border:2px solid var(--accent);border-radius:50%;display:flex;align-items:center;justify-content:center;font-family:"Oswald",sans-serif;font-weight:500;font-size:19px;color:var(--white)}
.copyright{left:1040px;top:2660px;width:130px;text-align:center;font-size:11px;color:var(--muted)}
</style>
</head>
<body>

<aside class="abs sidebar">
  <div class="side-block" style="top:0">
    <div class="brand">Brennwerk</div>
    <ul class="side-nav">
      <li class="current">COFFEE</li><li>SHOP</li><li>CONTACT</li><li>ABOUT</li>
      <li class="gap">SIGN UP</li><li>LOG IN</li>
    </ul>
    <div class="side-social"><span></span><span></span><span></span></div>
  </div>
  <div class="side-block" style="top:1020px">
    <div class="brand">Brennwerk</div>
    <ul class="side-nav">
      <li class="current">COFFEE</li><li>SHOP</li><li>CONTACT</li><li>ABOUT</li>
      <li class="gap">SIGN UP</li><li>LOG IN</li>
    </ul>
    <div class="side-social"><span></span><span></span><span></span></div>
  </div>
  <div class="side-block" style="top:2040px">
    <div class="brand">Brennwerk</div>
    <ul class="side-nav">
      <li class="current">COFFEE</li><li>SHOP</li><li>CONTACT</li><li>ABOUT</li>
      <li class="gap">SIGN UP</li><li>LOG IN</li>
    </ul>
    <div class="side-social"><span></span><span></span><span></span></div>
  </div>
</aside>

<section class="abs hero" role="img" aria-label="Cup of coffee on a wooden table beside a sack of spilled roasted coffee beans"></section>
<h1 class="abs hero-title">LIGHT ROASTED<br>COFFEE</h1>

<p class="abs kicker" style="left:268px;top:630px">What Happens Here</p>
<h2 class="abs heading" style="left:268px;top:668px">COFFEES WE PRODUCED</h2>
<div class="abs rule" style="left:268px;top:746px"></div>

<div class="abs product-img" style="left:268px;background:linear-gradient(180deg,#cfc8be 0%,#8a6a4e 60%,#3a2517 100%)" role="img" aria-label="Cup of coffee on a saucer with beans"></div>
<div class="abs product-img" style="left:580px;background:linear-gradient(160deg,#7a4a2a 0%,#4a2a16 50%,#2a170c 100%)" role="img" aria-label="Close-up of roasted coffee beans"></div>
<div class="abs product-img" style="left:888px;background:linear-gradient(200deg,#c9b79c 0%,#6b4a2e 55%,#2c1a0e 100%)" role="img" aria-label="Burlap sack spilling coffee beans"></div>

<div class="abs product" style="left:268px"><h3>PRODUCT NAME<span class="price">€ 120</span></h3><p>Freshly roasted beans from small farms, slow roasted in small batches for a smooth body and a sweet, clean finish.</p><div class="more">READ MORE</div></div>
<div class="abs product" style="left:580px"><h3>PRODUCT NAME<span class="price">€ 120</span></h3><p>Freshly roasted beans from small farms, slow roasted in small batches for a smooth body and a sweet, clean finish.</p><div class="more">READ MORE</div></div>
<div class="abs product" style="left:888px"><h3>PRODUCT NAME<span class="price">€ 120</span></h3><p>Freshly roasted beans from small farms, slow roasted in small batches for a smooth body and a sweet, clean finish.</p><div class="more">READ MORE</div></div>

<div class="abs arrows" style="left:666px;top:1250px">
  <svg viewBox="0 0 34 20"><path d="M32 10H3M10 3L3 10l7 7" fill="none" stroke="#9a9a9a" stroke-width="2"/></svg>
  <svg viewBox="0 0 34 20"><path d="M2 10h29M24 3l7 7-7 7" fill="none" stroke="#9a9a9a" stroke-width="2"/></svg>
</div>

<section class="abs about" role="img" aria-label="Dark backdrop with a coffee cup on a table"></section>
<div class="abs about-img" role="img" aria-label="Coffee pouring into a white cup"></div>
<p class="abs kicker" style="left:648px;top:1460px">About Us</p>
<h2 class="abs heading" style="left:648px;top:1496px;font-size:48px">WHO WE ARE</h2>
<div class="abs rule" style="left:648px;top:1580px"></div>
<p class="abs about-text">We are a small roastery with no cafe. We source green coffee from trusted farms and roast it in small batches every week. Our beans go to dealers, offices and home brewers who care about taste and freshness.</p>
<span class="abs btn" style="left:648px;top:1716px;width:116px;height:30px;line-height:30px;font-size:13px">READ MORE</span>

<p class="abs kicker" style="left:0;width:1432px;text-align:center;top:1940px">Type of Variety</p>
<h2 class="abs heading" style="left:0;width:1432px;text-align:center;top:1972px">ROASTED &nbsp;COFFEES</h2>
<div class="abs rule" style="left:684px;top:2050px"></div>

<svg class="abs" style="left:270px;top:2200px;width:34px;height:20px" viewBox="0 0 34 20"><path d="M32 10H3M10 3L3 10l7 7" fill="none" stroke="#9a9a9a" stroke-width="2"/></svg>
<div class="abs roast-img" style="left:328px;width:244px;background:linear-gradient(150deg,#8a5a34 0%,#5a3820 50%,#3a2212 100%)" role="img" aria-label="Roasted beans with a wooden scoop"></div>
<div class="abs roast-img" style="left:592px;width:248px;background:linear-gradient(150deg,#2a2a2a 0%,#3a2a20 100%)" role="img" aria-label="Darkened coffee beans"></div>
<div class="abs roast-label">LIGHT ROASTED<small>Coffee</small></div>
<div class="abs roast-img" style="left:852px;width:244px;background:linear-gradient(150deg,#c48050 0%,#8a4e2a 50%,#4a2814 100%)" role="img" aria-label="Coffee beans falling from a roaster"></div>
<svg class="abs" style="left:1128px;top:2200px;width:34px;height:20px" viewBox="0 0 34 20"><path d="M2 10h29M24 3l7 7-7 7" fill="none" stroke="#9a9a9a" stroke-width="2"/></svg>

<span class="abs btn" style="left:572px;top:2370px;width:288px;height:42px;line-height:42px">CONTACT US FOR BUSINESS</span>

<footer class="abs footer"></footer>
<h4 class="abs foot-head" style="left:268px;top:2548px">USEFULL LINKS</h4>
<ul class="abs foot-list" style="left:268px;top:2584px"><li>Coffee</li><li>Shop</li><li>Contact</li><li>About</li></ul>
<ul class="abs foot-list" style="left:410px;top:2584px"><li>Imprint</li><li>Privacy</li></ul>
<h4 class="abs foot-head" style="left:592px;top:2548px">CONTACT US</h4>
<ul class="abs foot-list" style="left:592px;top:2584px;line-height:20px"><li>1234 Roaster Street,</li><li>New York</li><li style="margin-top:10px">info@brennwerk.com</li><li>1-000-123-4567</li></ul>
<h4 class="abs foot-head" style="left:852px;top:2548px">FIND US ON</h4>
<div class="abs foot-social" style="left:852px;top:2588px"><span></span><span></span><span></span></div>
<div class="abs foot-brand">Brennwerk</div>
<p class="abs copyright">© Copyright 2018</p>

</body>
</html>
```